Clean bold and classy business card front and back
Kwr can be the logo
My name Trent Holloman as owner
Phone email and address
Owner Trent Holloman
Phone 8505550147
Email ridgelineinsulate@mailnest.example
Address170 frank pais rd Havana fl 32399

Industry/Entity Type

Business

Contact Information for Business Card

Owner Trent Holloman
Phone 8505550147

Requirements
Must have
• Keystone wall render under Kwr logo
Nice to have
• Bold and clean. Maybe use Kwr as logo and name under it. Have logo on one side and info on the other side with logo also
• Put a pic up. It doesn't have to be that but something that can be used
• Try some fancy fonts also

```html
<!DOCTYPE html>
<html lang="en">
<head>
<meta charset="utf-8">
<title>Keystone Wall Render – Business Card</title>
<link rel="stylesheet" href="https://fonts.googleapis.com/css2?family=Roboto:wght@300;400;700&display=swap">
<style>
  :root {
    --page-bg: #ecebe8;
    --card-white: #ffffff;
    --card-white-edge: #e6e8ea;
    --brand-blue: #35aedb;
    --brand-blue-deep: #0d86c2;
    --brand-blue-light: #1aa3d9;
    --logo-ink: #4a5560;
    --logo-ink-back: #0b5f8f;
    --text-grey: #6d7378;
    --accent-orange: #f08a2c;
  }
  * { box-sizing: border-box; margin: 0; padding: 0; }
  html, body {
    width: 1200px; height: 1023px; overflow: hidden;
    background: var(--page-bg);
    font-family: "Roboto", Arial, sans-serif;
  }
  .canvas { position: relative; width: 1200px; height: 1023px; }

  .card {
    position: absolute; width: 640px; height: 365px;
    border-radius: 3px;
    box-shadow: 0 10px 28px rgba(0,0,0,0.18);
    overflow: hidden;
  }

  /* Logo lockup: initials with the company name set beneath */
  .logo {
    display: flex; align-items: center; gap: 12px;
  }
  .logo-dot {
    width: 20px; height: 20px; border-radius: 50%;
    background: var(--brand-blue); flex: none;
  }
  .logo-text {
    display: flex; flex-direction: column;
    font-weight: 700; color: var(--logo-ink);
    line-height: 1;
  }
  .logo-initials { font-size: 52px; letter-spacing: 2px; }
  .logo-name { font-size: 15px; letter-spacing: 1.5px; margin-top: 6px; white-space: nowrap; }

  /* Front */
  .card-front {
    left: 80px; top: 70px;
    background: radial-gradient(ellipse at 40% 40%, var(--card-white) 45%, var(--card-white-edge) 100%);
  }
  .card-front .logo { position: absolute; left: 44px; top: 58px; }

  .name-band {
    position: absolute; left: 300px; right: 0; top: 62px; height: 56px;
    background: var(--brand-blue);
    display: flex; align-items: center; padding-left: 22px;
    color: #fff;
  }
  .name-band .person { font-weight: 700; font-size: 27px; white-space: nowrap; }
  .name-band .divider { width: 2px; height: 32px; background: #fff; margin: 0 12px; }
  .name-band .role { font-weight: 300; font-size: 21px; }

  .contact-list {
    position: absolute; left: 150px; top: 222px;
    list-style: none;
  }
  .contact-list li {
    display: flex; align-items: center; gap: 12px;
    font-size: 21px; font-weight: 400; color: var(--text-grey);
    height: 36px; white-space: nowrap;
  }
  .contact-list svg { width: 16px; height: 16px; flex: none; }

  /* Back */
  .card-back {
    left: 480px; top: 588px;
    background: radial-gradient(ellipse at 40% 30%, var(--brand-blue-light) 0%, var(--brand-blue-deep) 100%);
    display: flex; align-items: center; justify-content: center;
  }
  .card-back .logo-dot { width: 28px; height: 28px; background: var(--accent-orange); }
  .card-back .logo-text { color: var(--logo-ink-back); }
  .card-back .logo-initials { font-size: 84px; letter-spacing: 3px; }
  .card-back .logo-name { font-size: 24px; letter-spacing: 2px; margin-top: 8px; }
</style>
</head>
<body>
<main class="canvas">

  <section class="card card-front" aria-label="Business card front">
    <div class="logo">
      <span class="logo-dot"></span>
      <span class="logo-text">
        <span class="logo-initials">KWR</span>
        <span class="logo-name">Keystone Wall Render</span>
      </span>
    </div>

    <div class="name-band">
      <span class="person">Trent Holloman</span>
      <span class="divider"></span>
      <span class="role">Owner</span>
    </div>

    <ul class="contact-list">
      <li>
        <svg viewBox="0 0 16 16" aria-hidden="true"><rect x="4" y="1" width="8" height="14" rx="1.5" fill="var(--brand-blue)"/><rect x="5.5" y="3" width="5" height="8" fill="#fff"/></svg>
        8505550147
      </li>
      <li>
        <svg viewBox="0 0 16 16" aria-hidden="true"><rect x="1" y="3" width="14" height="10" fill="var(--brand-blue)"/><path d="M1 3 L8 9 L15 3" stroke="#fff" stroke-width="1.3" fill="none"/></svg>
        ridgelineinsulate@mailnest.example
      </li>
      <li>
        <svg viewBox="0 0 16 16" aria-hidden="true"><path d="M8 15 C4 10 3 8 3 6 A5 5 0 0 1 13 6 C13 8 12 10 8 15Z" fill="var(--brand-blue)"/><circle cx="8" cy="6" r="2" fill="#fff"/></svg>
        428 Dunmore Ct Havana FL 32399
      </li>
    </ul>
  </section>

  <section class="card card-back" aria-label="Business card back">
    <div class="logo">
      <span class="logo-dot"></span>
      <span class="logo-text">
        <span class="logo-initials">KWR</span>
        <span class="logo-name">Keystone Wall Render</span>
      </span>
    </div>
  </section>

</main>
</body>
</html>
```